Marlow Estate Group (Real Estate and Investment)

A high end, clean design.
We are a real estate company with sales, asset management and investment divisions. We want to use a black and white scheme which is really high end feel. The back of the card can just be the logo (black background with the white writing) as we will probably emboss this when we print)

Target Market(s)

High level investors, high end houses for sale

Industry/Entity Type

Business

Contact Information for Business Card

Name, position, phone number and email address
Ben Marlow, Managing Director, 0438926057 and ben@marlowestate.com.au

Requirements
Must have
• Back of the card to be the black background with the white writing (as per the attached images). Would like the capacity to emboss the writing and logo

```html
<!DOCTYPE html>
<html lang="en">
<head>
<meta charset="utf-8">
<title>Marlow Estate Group – Business Card</title>
<link rel="stylesheet" href="https://fonts.googleapis.com/css2?family=Montserrat:wght@400;500;600&display=swap">
<style>
  :root {
    --stage: #e9e9e7;
    --card-black: #141414;
    --card-black-soft: #262626;
    --card-white: #ffffff;
    --card-white-shade: #ececec;
    --ink: #2b2b2b;
    --ink-light: #f4f4f4;
    --ink-muted: #bdbdbd;
    --tab: #1c1c1c;
    --tab-edge: #2e2e2e;
  }
  * { box-sizing: border-box; margin: 0; padding: 0; }
  html, body {
    width: 1200px; height: 843px; overflow: hidden;
    background: var(--stage);
    font-family: "Montserrat", Arial, sans-serif;
  }
  .canvas { position: relative; width: 1200px; height: 843px; }

  .card {
    position: absolute;
    width: 600px; height: 366px;
    border-radius: 26px;
    overflow: hidden;
    box-shadow: 0 14px 30px rgba(0,0,0,.18);
  }

  /* Back of card */
  .card-back { left: 110px; top: 40px; background: var(--card-black); }
  .card-back .pattern-field {
    position: absolute; inset: 0;
    background: linear-gradient(135deg, var(--card-black-soft) 0%, var(--card-black) 55%, #0c0c0c 100%);
  }
  .card-back .back-brand {
    position: absolute; left: 0; right: 0; top: 150px;
    text-align: center; color: var(--ink-light);
  }
  .back-brand .wordmark {
    font-size: 30px; font-weight: 500; letter-spacing: .5px; white-space: nowrap;
  }
  .back-brand .web {
    margin-top: 6px; font-size: 15px; font-weight: 400; letter-spacing: 2.6px;
  }

  /* Front of card */
  .card-front {
    left: 490px; top: 437px;
    background: linear-gradient(160deg, var(--card-white) 55%, var(--card-white-shade) 100%);
  }
  .front-brand {
    position: absolute; left: 24px; top: 124px; width: 270px;
    text-align: center; color: var(--ink);
  }
  .front-brand .mark-circle {
    width: 70px; height: 70px; margin: 0 auto 16px;
    border: 2px solid var(--ink); border-radius: 50%;
  }
  .front-brand .wordmark {
    font-size: 18px; font-weight: 500; letter-spacing: .2px; white-space: nowrap;
  }

  .contact-tab {
    position: absolute; left: 305px; right: 0; top: 92px; height: 204px;
    background: var(--tab);
    border-radius: 16px 0 0 16px;
    border: 1px solid var(--tab-edge); border-right: 0;
    padding: 22px 0 0 26px;
    color: var(--ink-light);
  }
  .contact-tab .person-name {
    font-size: 21px; font-weight: 600; letter-spacing: .6px; line-height: 1.2;
  }
  .contact-tab .person-role {
    margin: 4px 0 12px;
    font-size: 12px; font-weight: 400; letter-spacing: 1.6px;
    text-transform: uppercase; color: var(--ink-muted);
  }
  .contact-list { list-style: none; }
  .contact-list li {
    display: flex; align-items: center; gap: 10px;
    font-size: 15px; line-height: 1.7; white-space: nowrap;
  }
  .contact-list svg { width: 14px; height: 14px; flex: none; fill: var(--ink-light); }
</style>
</head>
<body>
<main class="canvas">

  <section class="card card-back" aria-label="Card back">
    <div class="pattern-field" role="img" aria-label="Subtle tonal repeat pattern of the brand symbol on black"></div>
    <div class="back-brand">
      <p class="wordmark">MARLOW ESTATE GROUP</p>
      <p class="web">www.marlowestate.com.au</p>
    </div>
  </section>

  <section class="card card-front" aria-label="Card front">
    <div class="front-brand">
      <div class="mark-circle"></div>
      <p class="wordmark">MARLOW ESTATE GROUP</p>
    </div>

    <div class="contact-tab">
      <p class="person-name">BEN MARLOW</p>
      <p class="person-role">Managing Director</p>
      <ul class="contact-list">
        <li>
          <svg viewBox="0 0 16 16" aria-hidden="true"><path d="M3.6 1.2 5.8 3.6c.4.4.4 1 0 1.4L4.7 6.1c.9 1.9 2.4 3.4 4.3 4.3l1.1-1.1c.4-.4 1-.4 1.4 0l2.4 2.2c.4.4.4 1 0 1.4l-1.2 1.2c-.6.6-1.5.8-2.3.5C6.2 13.3 2.7 9.8 1.4 5.6c-.3-.8-.1-1.7.5-2.3Z"/></svg>
          0438926057
        </li>
        <li>
          <svg viewBox="0 0 16 16" aria-hidden="true"><path d="M1 3h14v1.2L8 9 1 4.2Zm0 2.6 7 4.8 7-4.8V13H1Z"/></svg>
          ben@marlowestate.com.au
        </li>
        <li>
          <svg viewBox="0 0 16 16" aria-hidden="true"><circle cx="8" cy="8" r="7" fill="none" stroke="#f4f4f4" stroke-width="1.4"/><ellipse cx="8" cy="8" rx="3" ry="7" fill="none" stroke="#f4f4f4" stroke-width="1.2"/><path d="M1 8h14" stroke="#f4f4f4" stroke-width="1.2"/></svg>
          www.marlowestate.com.au
        </li>
      </ul>
    </div>
  </section>

</main>
</body>
</html>
```